Modern Spot UV Business Card design

We are a relatively new real estate agency. We need a business card that reflects the professionalism and prestige of our company but is also modern and fresh, based around our logo.
We would love to utilise spot UV.
Happy to let the designers use their imagination and see what they come up with (we're not very creative, so have no ideas for you, sorry) :-)
We'd like one for each staff member, but I've just provided one staff members photo here to avoid confusion.

Target Market(s)

Families

Industry/Entity Type

Real Estate Agent

Contact Information for Business Card

Dale Verco - Director & Principal
Mobile: 0491 627 540
Email: dale.verco@vbrokers.example.au
Phone: (08) 8374 6150
Fax: (08) 8374 6198
www.vercobrokersproperty.example.au

Font styles to use
Other font styles liked:
• Kabel Dm BT

Requirements
Must have
• Contact details, logo, photo, spot UV
Nice to have
• Modern interesting features that will make people comment. Nothing too feminine nor too masculine.
Should not have
• No houses! Nothing typical of a real estate agent.

```html
<!DOCTYPE html>
<html lang="en">
<head>
<meta charset="utf-8">
<title>Verco Brokers Property – Business Card</title>
<link rel="stylesheet" href="https://fonts.googleapis.com/css2?family=Montserrat:wght@400;600;700&family=Questrial&display=swap">
<style>
  :root {
    --stage: #3a3a3c;
    --card-black: #1b1b1c;
    --uv-gloss: #2a2a2b;
    --uv-text: #6c6c6e;
    --paper: #ffffff;
    --ink: #1e1e1e;
    --band: #2b2b2c;
    --accent-blue: #2196e3;
    --muted: #7a7a7a;
    --photo-light: #d9d9db;
    --photo-dark: #4a4c50;
  }
  * { box-sizing: border-box; margin: 0; padding: 0; }
  html, body { width: 802px; height: 1200px; overflow: hidden; }
  body {
    background: var(--stage);
    font-family: "Montserrat", sans-serif;
    position: relative;
  }
  .card {
    position: absolute;
    left: 51px;
    width: 700px;
    height: 400px;
    overflow: hidden;
    box-shadow: 0 10px 30px rgba(0,0,0,.45);
  }
  .card--front { top: 120px; background: var(--card-black); }
  .card--back { top: 660px; background: var(--paper); }

  .uv-wave { position: absolute; inset: 0; }

  .brand {
    position: absolute;
    display: flex;
    align-items: center;
    gap: 10px;
  }
  .brand__name {
    font-family: "Montserrat", sans-serif;
    font-weight: 700;
    letter-spacing: -0.5px;
    white-space: nowrap;
  }
  .brand__mark { border-radius: 50%; flex: none; }
  .tagline {
    position: absolute;
    font-family: "Questrial", sans-serif;
    line-height: 1.05;
    letter-spacing: 1px;
    white-space: nowrap;
  }

  /* front */
  .card--front .brand { left: 110px; top: 130px; }
  .card--front .brand__name { font-size: 60px; color: var(--uv-text); }
  .card--front .brand__mark { width: 38px; height: 38px; background: var(--uv-text); }
  .card--front .tagline { left: 390px; top: 220px; font-size: 22px; color: var(--uv-text); border-left: 2px solid var(--uv-text); padding-left: 10px; }

  /* back */
  .card--back .brand { left: 120px; top: 58px; }
  .card--back .brand__name { font-size: 40px; color: var(--ink); }
  .card--back .brand__mark { width: 26px; height: 26px; background: var(--accent-blue); }
  .card--back .tagline { left: 368px; top: 110px; font-size: 14px; color: var(--muted); border-left: 1px solid var(--muted); padding-left: 7px; }

  .rule { position: absolute; left: 0; height: 4px; background: var(--accent-blue); }
  .rule--top { top: 148px; width: 700px; }
  .rule--mid { top: 266px; width: 470px; }
  .rule--bottom { top: 352px; width: 470px; }

  .contact-band {
    position: absolute;
    left: 0; top: 155px;
    width: 700px; height: 108px;
    background: var(--band);
    padding: 12px 0 0 112px;
    color: #fff;
  }
  .person { font-weight: 700; font-size: 17px; letter-spacing: .3px; margin-bottom: 6px; }
  .contact-list { list-style: none; }
  .contact-list li {
    display: flex; align-items: center; gap: 8px;
    font-weight: 600; font-size: 15px; line-height: 23px;
  }
  .icon { width: 13px; height: 13px; flex: none; }

  .online-list {
    position: absolute; left: 90px; top: 278px;
    list-style: none; color: var(--ink);
  }
  .online-list li {
    display: flex; align-items: center; gap: 8px;
    font-weight: 600; font-size: 15px; line-height: 30px;
  }

  .portrait {
    position: absolute;
    right: 20px; top: 170px;
    width: 230px; height: 230px;
    background: linear-gradient(180deg, var(--photo-light) 0%, #8a8c90 45%, var(--photo-dark) 100%);
  }
</style>
</head>
<body>

  <section class="card card--front" aria-label="Card front">
    <svg class="uv-wave" viewBox="0 0 700 400" aria-hidden="true">
      <path d="M0 400 L0 250 C120 180 240 140 330 170 C420 200 470 160 560 140 C640 125 700 170 700 240 L700 400 Z" fill="var(--uv-gloss)"/>
      <path d="M560 140 C640 125 700 170 700 240 L700 400 L610 400 C640 300 620 200 560 140 Z" fill="#232324"/>
    </svg>
    <div class="brand">
      <span class="brand__name">Verco Brokers</span>
      <span class="brand__mark"></span>
    </div>
    <p class="tagline">Guiding you toward<br>your next address</p>
  </section>

  <section class="card card--back" aria-label="Card back">
    <div class="brand">
      <span class="brand__name">Verco Brokers</span>
      <span class="brand__mark"></span>
    </div>
    <p class="tagline">Guiding you toward<br>your next address</p>

    <div class="rule rule--top"></div>
    <div class="contact-band">
      <p class="person">DALE VERCO-Director &amp; Principal</p>
      <ul class="contact-list">
        <li>
          <svg class="icon" viewBox="0 0 12 12"><rect x="3" y="0.5" width="6" height="11" rx="1" fill="none" stroke="var(--accent-blue)" stroke-width="1.3"/></svg>
          0491 627 540
        </li>
        <li>
          <svg class="icon" viewBox="0 0 12 12"><path d="M1 5 C1 2 11 2 11 5 L9 6 L8 4.5 L4 4.5 L3 6 Z M2.5 7 H9.5 L10 11 H2 Z" fill="var(--accent-blue)"/></svg>
          (08) 8374 6150
        </li>
        <li>
          <svg class="icon" viewBox="0 0 12 12"><rect x="3" y="1" width="6" height="3" fill="var(--accent-blue)"/><rect x="1" y="4.5" width="10" height="5" rx="1" fill="var(--accent-blue)"/><rect x="3" y="8" width="6" height="3" fill="#fff"/></svg>
          (08) 8374 6198
        </li>
      </ul>
    </div>
    <div class="rule rule--mid"></div>

    <ul class="online-list">
      <li>
        <svg class="icon" viewBox="0 0 12 12"><rect x="0.7" y="2.2" width="10.6" height="7.6" fill="none" stroke="var(--accent-blue)" stroke-width="1.2"/><path d="M0.7 2.2 L6 6.5 L11.3 2.2" fill="none" stroke="var(--accent-blue)" stroke-width="1.2"/></svg>
        dale.verco@vbrokers.example.au
      </li>
      <li>
        <svg class="icon" viewBox="0 0 12 12"><circle cx="6" cy="6" r="5.2" fill="none" stroke="var(--accent-blue)" stroke-width="1.2"/><ellipse cx="6" cy="6" rx="2.3" ry="5.2" fill="none" stroke="var(--accent-blue)" stroke-width="1"/><path d="M0.8 6 H11.2" stroke="var(--accent-blue)" stroke-width="1"/></svg>
        www.vercobrokersproperty.example.au
      </li>
    </ul>
    <div class="rule rule--bottom"></div>

    <div class="portrait" role="img" aria-label="Portrait photo of Dale Verco in a grey suit jacket and striped shirt"></div>
  </section>

</body>
</html>
```